Help keep hoosiers happy and at home!

We need a billboard designed for our Indiana based healthcare business called 'Willow Hearth Caregivers'. We administer a medicaid waiver program that provides support and financial aid to live in caregivers that take care of someone who would otherwise be in a nursing home or skilled nursing facility. Qualified caregivers could be eligible to receive up to 1200 dollars a month in tax free financial aid, as well as access to nursing support that helps manage any unexpected situations or changes in a care recipients condition or care routine. Our program empowers families to keep their loved ones at home and out of the nursing home. NOTE: We believe the tagline at the bottom of our logo is disproportionately small. We would like to see that tagline larger and easier to read. I look forward to seeing your design ideas!

Target Market(s)

Medicaid aged beneficiaries and caregivers.

Industry/Entity Type

Home Healthcare

Colors
0054AA
0677BA
7BADD7
CADEEF
E8F1F8

Requirements
Nice to have
• "Empowering friends and family to care for their loves ones at home. Eligible participants receive up to $15,000 a year, tax free."

```html
<!DOCTYPE html>
<html lang="en">
<head>
<meta charset="utf-8">
<title>Willow Hearth Caregivers – Billboard</title>
<link rel="stylesheet" href="https://fonts.googleapis.com/css2?family=Montserrat:wght@400;500;700&display=swap">
<style>
  :root {
    --navy: #2e3478;
    --brand-blue: #1b75bd;
    --link-blue: #0677ba;
    --paper: #ffffff;
    --panel-light: #fbfbfb;
    --ink-light: #ffffff;
  }
  html, body {
    margin: 0;
    padding: 0;
    width: 1200px;
    height: 1118px;
    overflow: hidden;
    background: var(--paper);
  }
  .canvas {
    position: relative;
    width: 1200px;
    height: 1118px;
    display: flex;
    align-items: center;
    justify-content: center;
  }
  .billboard {
    display: block;
    width: 1120px;
    height: 327px;
    font-family: "Montserrat", sans-serif;
  }
  .brand-name { fill: var(--navy); font-weight: 500; letter-spacing: 1px; }
  .brand-mark { fill: var(--navy); }
  .website { fill: var(--navy); font-weight: 400; }
  .website-strong { fill: var(--link-blue); font-weight: 700; }
  .message { fill: var(--ink-light); font-weight: 400; }
  .message-strong { font-weight: 700; }
  .callout { fill: var(--ink-light); font-weight: 400; }
</style>
</head>
<body>
<main class="canvas">
  <svg class="billboard" viewBox="0 0 1420 415" xmlns="http://www.w3.org/2000/svg" role="img" aria-label="Willow Hearth Caregivers billboard">
    <defs>
      <linearGradient id="paperShade" x1="0" y1="0" x2="1" y2="1">
        <stop offset="0" stop-color="#ffffff"/>
        <stop offset="1" stop-color="#f3f3f3"/>
      </linearGradient>
    </defs>

    <!-- brand side -->
    <rect class="brand-panel" x="0" y="0" width="1420" height="415" fill="url(#paperShade)"/>
    <circle class="brand-mark" cx="278" cy="95" r="34"/>
    <text class="brand-name" x="278" y="192" text-anchor="middle" font-size="46">Willow Hearth</text>
    <text class="brand-name" x="278" y="248" text-anchor="middle" font-size="46">Caregivers</text>
    <text class="website" x="278" y="362" text-anchor="middle" font-size="24">www.<tspan class="website-strong">willowhearth</tspan>caregivers.com</text>

    <!-- message side -->
    <polygon class="accent-stripe" points="690,0 1420,0 1420,415 557,415" fill="var(--navy)"/>
    <polygon class="message-panel" points="690,0 1420,0 1420,287 698,287 597,415" fill="var(--brand-blue)"/>

    <text class="message" x="1358" y="85" text-anchor="end" font-size="31">Empowering <tspan class="message-strong">friends and family</tspan> to care</text>
    <text class="message" x="1362" y="126" text-anchor="end" font-size="31">for <tspan class="message-strong">their loves ones at home</tspan>.</text>
    <text class="message" x="1362" y="188" text-anchor="end" font-size="31">Eligible participants receive up to</text>
    <text class="message message-strong" x="1367" y="238" text-anchor="end" font-size="42">$15,000 a year, tax free.</text>

    <text class="callout" x="1358" y="362" text-anchor="end" font-size="40">Call us today at <tspan class="message-strong">(800)555-0142</tspan></text>
  </svg>
</main>
</body>
</html>
```